Quote Cards With TK May 2025 for Instagram

I would like to put these quotes over one of the pictures attached; Instagram (new size: 4:5 (1080 x 1350 pixels) One Quote per picture, and I want the quote to be bold or easy to read as well. I provided a few reference graphics that I really like as examples below. In very small letters at the bottom add @TKBarlowOnline

All of the pictures are attached; you can pick any photo and add one quote to it; but no stock photography

```html
<!DOCTYPE html>
<html lang="en">
<head>
<meta charset="utf-8">
<title>Quote Cards With TK</title>
<link rel="stylesheet" href="https://fonts.googleapis.com/css2?family=Anton&family=Lobster&family=Poppins:wght@500;600;700;800&display=swap">
<style>
  :root {
    --pink: #f0068a;
    --pink-deep: #cc0066;
    --pink-glow: #ff3ea6;
    --yellow: #ffea00;
    --ink: #1c1c1c;
    --white: #ffffff;
  }
  * { box-sizing: border-box; margin: 0; padding: 0; }
  html, body { width: 1200px; height: 815px; overflow: hidden; background: var(--white); }
  body { position: relative; font-family: "Poppins", sans-serif; }

  .card {
    position: absolute;
    top: 89px;
    width: 501px;
    height: 626px;
    overflow: hidden;
    border: 1px solid #888;
  }
  .card--hormones { left: 67px; background: radial-gradient(circle at 50% 55%, var(--pink-glow) 0%, var(--pink) 40%, var(--pink-deep) 100%); }
  .card--tummy { left: 635px; background: var(--white); }

  .abs { position: absolute; }
  .layer-photo { z-index: 0; }
  .layer-text { z-index: 2; }

  /* Card 1 */
  .kicker {
    top: 36px; left: 0; width: 100%; text-align: center;
    color: var(--white); font-weight: 700; font-size: 26px; letter-spacing: 3px;
  }
  .script {
    font-family: "Lobster", cursive; color: var(--white); font-size: 84px; line-height: 1;
  }
  .script--belly { left: 40px; top: 96px; }
  .script--fat { left: 340px; top: 100px; }
  .photo--pointing {
    left: 32px; top: 74px; width: 453px; height: 291px;
    border-radius: 120px 120px 0 0;
    background: linear-gradient(180deg, rgba(42,20,32,0.55) 0%, rgba(20,10,16,0.85) 100%);
  }
  .band {
    top: 365px; left: 0; width: 100%; height: 106px; background: var(--white);
  }
  .band__lead {
    top: 14px; left: 0; width: 100%; text-align: center;
    color: var(--pink); font-weight: 700; font-size: 40px; line-height: 1.1;
  }
  .band__shout {
    top: 56px; left: 0; width: 100%; text-align: center;
    color: var(--ink); font-weight: 800; font-size: 35px; line-height: 1.1;
  }
  .fix-line {
    top: 487px; left: 0; width: 100%; text-align: center;
    color: var(--white); font-weight: 600; font-size: 58px; line-height: 1.1; letter-spacing: 1px;
  }
  .fix-check { left: 264px; top: 476px; }

  .handle {
    color: var(--white); font-weight: 500; font-size: 18px;
  }
  .card--hormones .handle { right: 40px; top: 580px; }

  /* Card 2 */
  .top-field {
    top: 0; left: 0; width: 100%; height: 378px;
    background: radial-gradient(circle at 40% 55%, var(--pink-glow) 0%, var(--pink) 40%, var(--pink-deep) 100%);
  }
  .photo--standing {
    left: 10px; top: 108px; width: 150px; height: 390px;
    border-radius: 75px 75px 40px 40px;
    background: linear-gradient(180deg, rgba(42,20,32,0.6) 0%, rgba(18,10,14,0.92) 60%, rgba(18,10,14,0.95) 100%);
  }
  .headline {
    top: 40px; right: 40px; color: var(--white);
    font-weight: 800; font-size: 64px; line-height: 1.1; letter-spacing: -0.5px;
  }
  .script--age { right: 38px; top: 100px; font-size: 64px; }
  .possible {
    top: 178px; right: 40px; color: var(--yellow);
    font-family: "Anton", sans-serif; font-size: 44px; line-height: 1.1;
  }
  .arrow-down { left: 303px; top: 230px; }
  .comment {
    top: 264px; left: 220px; color: var(--white);
    font-weight: 800; font-size: 36px; line-height: 1.1;
  }
  .bubble { left: 176px; top: 300px; }
  .bubble__text {
    top: 322px; left: 184px; width: 276px; text-align: center;
    color: var(--pink); font-weight: 800; font-size: 48px; line-height: 1.2; letter-spacing: -1px;
  }
  .offer {
    left: 41px; top: 474px; width: 417px; height: 152px;
    background: var(--pink); border-radius: 22px 22px 0 0;
  }
  .offer__line {
    left: 0; width: 100%; text-align: center; color: var(--white);
    font-weight: 700; font-size: 28px; line-height: 1.1; letter-spacing: -0.5px;
  }
  .offer__line--one { top: 30px; }
  .offer__line--two { top: 68px; }
  .card--tummy .handle { right: 36px; top: 114px; }
</style>
</head>
<body>

  <section class="card card--hormones">
    <div class="abs photo--pointing layer-photo" role="img" aria-label="Photo of TK in a sheer striped black top pointing down at her belly"></div>
    <p class="abs kicker layer-text">TIRED. MOODY. STUBBORN</p>
    <p class="abs script script--belly layer-text">Belly</p>
    <p class="abs script script--fat layer-text">Fat</p>

    <div class="abs band layer-text">
      <p class="abs band__lead">Your Hormones Are</p>
      <p class="abs band__shout">SCREAMING FOR HELP!</p>
    </div>

    <p class="abs fix-line layer-text">LET’S FIX THAT</p>
    <svg class="abs fix-check layer-text" width="40" height="60" viewBox="0 0 40 60" aria-hidden="true">
      <line x1="2" y1="3" x2="36" y2="3" stroke="var(--yellow)" stroke-width="4"/>
      <polyline points="4,30 15,50 34,9" fill="none" stroke="var(--yellow)" stroke-width="6"/>
    </svg>

    <p class="abs handle layer-text">@TKBarlowOnline</p>
  </section>

  <section class="card card--tummy">
    <div class="abs top-field layer-photo"></div>
    <div class="abs photo--standing layer-photo" role="img" aria-label="Photo of TK in a black long-sleeve outfit standing side-on and smiling"></div>

    <p class="abs headline layer-text">FLAT TUMMY</p>
    <p class="abs script script--age layer-text">in your 40s ?</p>
    <p class="abs possible layer-text">IT’S STILL POSSIBLE!</p>

    <svg class="abs arrow-down layer-text" width="20" height="32" viewBox="0 0 20 32" aria-hidden="true">
      <line x1="10" y1="1" x2="10" y2="29" stroke="var(--white)" stroke-width="2.5"/>
      <polyline points="2,21 10,29 18,21" fill="none" stroke="var(--white)" stroke-width="2.5"/>
    </svg>
    <p class="abs comment layer-text">COMMENT</p>

    <svg class="abs bubble layer-text" width="290" height="110" viewBox="0 0 290 110" aria-hidden="true">
      <path d="M42,18 H228 L244,4 L246,20 A42,42 0 0 1 246,104 H42 A42,42 0 0 1 42,18 Z"
            fill="var(--white)" stroke="var(--pink)" stroke-width="4" stroke-linejoin="round"/>
    </svg>
    <p class="abs bubble__text layer-text">BYE BELLY</p>

    <div class="abs offer layer-text">
      <p class="abs offer__line offer__line--one">TO GET THE 10 SECRETS</p>
      <p class="abs offer__line offer__line--two">— TO A FLATTER TUMMY —</p>
      <p class="abs handle">@TKBarlowOnline</p>
    </div>
  </section>

</body>
</html>
```